tidal box

TIDAL BOX mobile technology servicesPhone and tablet repairs, screens data recovery.

Industry/Entity Type

Data Recovery

Contact Information for Business Card

0491 573 086

Colors
33a6d7
f04a50
0a90cc
e34197

Requirements
Must have
• Liam hardy
Nice to have
• White background

```html
<!DOCTYPE html>
<html lang="en">
<head>
<meta charset="utf-8">
<title>Tidal Box – Business Card</title>
<link rel="stylesheet" href="https://fonts.googleapis.com/css2?family=Jost:wght@500&family=Libre+Bodoni:wght@700&family=Sorts+Mill+Goudy&display=swap">
<style>
  :root {
    --cyan: #3fd3f1;
    --cyan-soft: #bdf0fa;
    --coral: #ff2a55;
    --coral-soft: #ffc2cf;
    --ink: #111111;
    --stone: #8a8a8a;
    --paper: #ffffff;
    --frame: #1a1a1a;
  }
  html, body {
    margin: 0;
    padding: 0;
    width: 1200px;
    height: 801px;
    overflow: hidden;
    background: var(--paper);
  }
  .sheet {
    position: relative;
    width: 1200px;
    height: 801px;
    box-sizing: border-box;
    border: 1.5px solid var(--frame);
    background: var(--paper);
  }
  .card {
    position: absolute;
    left: 150px;
    top: 150px;
    width: 900px;
    height: 501px;
    box-sizing: border-box;
    border-left: 1.5px solid var(--frame);
    border-right: 1.5px solid var(--frame);
    background: var(--paper);
  }
  .card__corner {
    position: absolute;
    left: 0;
    width: 900px;
  }
  .card__corner--top { top: 0; height: 152px; }
  .card__corner--bottom { bottom: 0; height: 151px; }
  .identity__brand,
  .identity__name,
  .identity__phone {
    position: absolute;
    right: 485px;
    margin: 0;
    line-height: 1;
    white-space: nowrap;
    text-align: right;
  }
  .identity__brand {
    top: 82px;
    font-family: "Jost", sans-serif;
    font-weight: 500;
    font-size: 76px;
    letter-spacing: 0.5px;
    color: var(--coral);
  }
  .identity__name {
    top: 178px;
    font-family: "Jost", sans-serif;
    font-weight: 500;
    font-size: 38px;
    color: var(--cyan);
  }
  .identity__phone {
    top: 226px;
    right: 500px;
    font-family: "Libre Bodoni", serif;
    font-weight: 700;
    font-size: 19px;
    letter-spacing: 1.5px;
    color: var(--ink);
  }
  .services {
    position: absolute;
    right: 41px;
    top: 300px;
    margin: 0;
    text-align: right;
    font-family: "Sorts Mill Goudy", serif;
    font-size: 29px;
    line-height: 38px;
    color: var(--stone);
    white-space: nowrap;
  }
</style>
</head>
<body>
<div class="sheet">
  <section class="card">
    <svg class="card__corner card__corner--top" viewBox="0 0 900 152" role="img" aria-label="Cyan stepped stripe pattern in the top right corner">
      <defs>
        <linearGradient id="cyanFade" x1="0" y1="0" x2="1" y2="0">
          <stop offset="0" stop-color="var(--cyan-soft)"/>
          <stop offset="1" stop-color="var(--cyan)"/>
        </linearGradient>
      </defs>
      <polygon points="0,0 900,0 900,152" fill="url(#cyanFade)"/>
    </svg>
    <svg class="card__corner card__corner--bottom" viewBox="0 0 900 151" role="img" aria-label="Coral stepped stripe pattern in the bottom left corner">
      <defs>
        <linearGradient id="coralFade" x1="0" y1="0" x2="1" y2="0">
          <stop offset="0" stop-color="var(--coral)"/>
          <stop offset="1" stop-color="var(--coral-soft)"/>
        </linearGradient>
      </defs>
      <polygon points="0,0 900,151 0,151" fill="url(#coralFade)"/>
    </svg>

    <header class="identity">
      <h1 class="identity__brand">TIDAL BOX</h1>
      <p class="identity__name">Liam Hardy</p>
      <p class="identity__phone">0491 573 086</p>
    </header>

    <p class="services">
      Mobile Technology Services<br>
      Phone and Tablet Repairs,<br>
      Screens Data Recovery
    </p>
  </section>
</div>
</body>
</html>
```